Anzeigengestaltung für eine Hausarztpraxis
Zielgruppe
Wir sind eine Hausarztpraxis mit zwei Standorten und suchen eine Ärztin oder einen Arzt zur Anstellung in der klassischen Hausarzt Medizin am Standort Dorfmatt
Aufgabenstellung
Bitte beachtet den Text im Anhang, der ist schon vorgegeben. (Anzeigentext)
Wir suchen ein ruhiges, hochwertiges Layout für eine Stellenanzeige einer Hausarztpraxis in einem historischen Gebäude.
Der Text steht im Vordergrund, das Design soll zurückhaltend, klar und wertig sein.
Bitte keine Icons, keine bunten Farben, keine verspielten Elemente.
Gerne viel Weissraum, klare Typografie, ruhige Anmutung.
Schrift: Garamond für den Fliesstext (bereits gewählt).
Das Layout soll sowohl als PDF wie auch online funktionieren.
Optional: ein sehr dezentes grafisches Element oder eine ruhige Bildanmutung (z. B. Struktur, Licht, Architekturdetail).

```html
<!DOCTYPE html>
<html lang="de">
<head>
<meta charset="utf-8">
<title>Hausarztpraxis Dorfmatt – Stellenanzeige</title>
<link href="https://fonts.googleapis.com/css2?family=EB+Garamond:wght@400;500;600;700&display=swap" rel="stylesheet">
<style>
  :root {
    --paper: #efe9df;
    --sand-light: #ece5d8;
    --sand-mid: #d9d0c0;
    --stone: #c7bdab;
    --panel: rgba(255, 255, 255, 0.72);
    --ink: #2f2f2f;
    --ink-soft: #3d3d3d;
  }
  * { margin: 0; padding: 0; box-sizing: border-box; }
  html, body {
    width: 1200px;
    height: 800px;
    overflow: hidden;
    background: var(--paper);
  }
  .ad {
    position: relative;
    width: 1200px;
    height: 800px;
    overflow: hidden;
    font-family: "EB Garamond", Garamond, serif;
    color: var(--ink);
  }
  .ad__backdrop {
    position: absolute;
    inset: 0;
    background:
      radial-gradient(ellipse 60% 45% at 50% 30%, #f4efe6 0%, transparent 70%),
      linear-gradient(180deg, var(--sand-light) 0%, var(--sand-mid) 55%, var(--stone) 100%);
  }
  .ad__panel {
    position: absolute;
    left: 53px;
    top: 115px;
    width: 1096px;
    height: 630px;
    background: var(--panel);
    text-align: center;
  }
  .ad__title {
    position: absolute;
    top: 54px;
    left: 0;
    right: 0;
    font-size: 47px;
    font-weight: 700;
    letter-spacing: 1px;
    color: var(--ink);
  }
  .ad__subtitle {
    position: absolute;
    top: 146px;
    left: 0;
    right: 0;
    font-size: 31px;
    font-weight: 500;
    letter-spacing: 0.3px;
    color: var(--ink-soft);
  }
  .ad__body {
    position: absolute;
    top: 240px;
    left: 110px;
    right: 120px;
    font-size: 21px;
    line-height: 26px;
    color: var(--ink-soft);
  }
  .ad__body p + p { margin-top: 25px; }
  .ad__closing {
    position: absolute;
    top: 494px;
    left: 0;
    right: 0;
    font-size: 24px;
    font-weight: 600;
  }
  .ad__contact {
    position: absolute;
    top: 531px;
    left: 0;
    right: 0;
    font-size: 20px;
  }
  .ad__contact strong { font-weight: 700; }
  .ad__locations {
    position: absolute;
    top: 588px;
    left: 0;
    right: 0;
    font-size: 20px;
    color: var(--ink-soft);
  }
</style>
</head>
<body>
  <main class="ad">
    <div class="ad__backdrop" role="img" aria-label="Verblasste Fotografie eines historischen Praxisgebäudes mit Kiesplatz und Garten in warmen Sandtönen"></div>
    <section class="ad__panel">
      <h1 class="ad__title">HAUSARZTPRAXIS DORFMATT</h1>
      <h2 class="ad__subtitle">VERSTÄRKUNG GESUCHT: ÄRZTIN / ARZT (m/w/d)</h2>
      <div class="ad__body">
        <p>Wir sind eine etablierte Hausarztpraxis mit zwei Standorten und suchen zur Erweiterung unseres Teams in Dorfmatt eine engagierte Ärztin / einen engagierten Arzt in Teilzeit. Unsere Praxis in Dorfmatt ist ruhig gelegen und modern. Sie befindet sich in einem historischen Gebäude mit liebevoll gestaltetem Innenhof.</p>
        <p>Wir bieten Ihnen attraktive Anstellungsbedingungen, flexible und familienfreundliche Arbeitszeiten und Möglichkeiten zur Weiterbildung. Erfahrung im Fach Allgemeine Innere Medizin ist von Vorteil, aber auch motivierte Berufseinsteiger sind Teil unseres Teams und gestalten die Zukunft der Hausarztmedizin in Dorfmatt mit.</p>
      </div>
      <p class="ad__closing">Wir freuen uns auf Ihre Bewerbung.</p>
      <p class="ad__contact"><strong>Kontakt:</strong> Dr. med. [Nachname] E-Mail: bewerbung@praxis-dorfmatt.ch, Tel: [Telefonnummer]</p>
      <p class="ad__locations">Standorte: Dorfmatt &amp; [Zweiter Standortname]</p>
    </section>
  </main>
</body>
</html>
```